Business Card Design Project

Design a business card for a new entity that is in the OTC (over-the-counter-derivative brokering business-Financial Services.
The card should be clean a professional looking. We encourage designers to think pro-actively, fresh and innovative, but also keep in mind that only 2 things are important. a)that the card look professional b)that it is somehow memorable.

We have a new logo which we will upload and will want the Trident symbol in the logo to be raised OR not have the symbol raised and plan on having the word " BROKERAGE SERVICES" raised that stands out and will look sharp.

Along with uploading the new logo which MUST be incorperated, I am also going to upload 3 different business cards of other businesses to use only as guild-lines since I think they are clean and professional looking BUT I encourage all to be pro-active and creative on their own.

Industry/Entity Type

Business

Requirements
Must have
• 1. MUST HAVE THE NEW LOGO WHICH WILL BE UPLOADED
2. MUST HAVE A VERSION SIMILAR TO THE 3 DIFFERENT BUSINESS CARDS I WILL UPLOAD, BUT EACH DESIGNER MUST ONLY THESE THIS FORMAT AS A BACK-UP AND BE CREATIVE ON THEIR OWN FIRST. ALSO WHEN LOOKING AT THE CARDS WHICH I UPLOAD TO USE AS A GUILD-LINE KEEP IN MIND THAT THESE ARE KESTRAVEL 300 COMPANIES SO DO NOT MIMIC ONLY USE FOR IDEAS.
Nice to have
• these are the 3 different other biz cards to look at for some reference

```html
<!DOCTYPE html>
<html lang="en">
<head>
<meta charset="utf-8">
<title>Corvane Brokerage Services – Business Card</title>
<link rel="stylesheet" href="https://fonts.googleapis.com/css2?family=Saira:wght@400;500;600&display=swap">
<style>
  :root {
    --backdrop: #3b3b3d;
    --card-white: #ffffff;
    --card-silver-light: #f4f4f5;
    --card-silver-mid: #e2e2e4;
    --card-silver-dark: #cfcfd2;
    --ink: #2a2a2c;
    --ink-soft: #5a5a5e;
    --gold: #c9a24a;
    --label: #ffffff;
    --rule: #4a4a4c;
  }
  * { margin: 0; padding: 0; box-sizing: border-box; }
  html, body {
    width: 1200px;
    height: 900px;
    overflow: hidden;
  }
  body {
    position: relative;
    background: var(--backdrop);
    font-family: "Saira", "Arial", sans-serif;
    color: var(--ink);
  }
  .card {
    position: absolute;
    top: 300px;
    width: 525px;
    height: 300px;
    border-radius: 18px;
    overflow: hidden;
  }

  /* Front card */
  .card-front {
    left: 58px;
    background: var(--card-white);
  }
  .card-front .info-band {
    position: absolute;
    left: 0;
    top: 147px;
    width: 100%;
    height: 153px;
    background: linear-gradient(180deg, var(--card-silver-mid) 0%, var(--card-silver-light) 55%, var(--card-silver-mid) 100%);
  }
  .card-front .band-notch {
    position: absolute;
    left: 68px;
    top: 147px;
    width: 34px;
    height: 18px;
  }
  .brand-lockup {
    position: absolute;
    left: 48px;
    top: 40px;
    display: flex;
    align-items: center;
    gap: 22px;
  }
  .brand-dot {
    width: 64px;
    height: 64px;
    border-radius: 50%;
    background: var(--ink);
    flex: none;
  }
  .brand-name {
    font-weight: 500;
    color: var(--ink);
    line-height: 1;
  }
  .brand-name .brand-main {
    display: block;
    font-size: 44px;
    letter-spacing: 2px;
  }
  .brand-name .brand-sub {
    display: block;
    margin-top: 6px;
    font-size: 12px;
    letter-spacing: 5.2px;
  }

  .contact-person {
    position: absolute;
    left: 48px;
    top: 178px;
  }
  .person-name {
    font-size: 17px;
    font-weight: 500;
    letter-spacing: 0.3px;
  }
  .person-role {
    font-size: 12px;
    margin-left: 6px;
  }
  .contact-lines {
    margin-top: 6px;
    font-size: 12px;
    line-height: 16px;
  }
  .contact-lines .label { color: var(--label); }
  .website {
    margin-top: 9px;
    font-size: 15px;
    font-weight: 600;
    letter-spacing: 0.3px;
  }
  .column-rule {
    position: absolute;
    left: 311px;
    top: 183px;
    width: 1px;
    height: 87px;
    background: var(--rule);
  }
  .contact-address {
    position: absolute;
    left: 330px;
    top: 180px;
    font-size: 12px;
    line-height: 15px;
    letter-spacing: 0.3px;
  }
  .contact-address .phones { margin-top: 16px; }
  .contact-address .label { color: var(--label); }

  /* Back card */
  .card-back {
    left: 617px;
    background: linear-gradient(160deg, var(--card-silver-light) 0%, var(--card-white) 30%, var(--card-silver-mid) 65%, var(--card-silver-dark) 100%);
    text-align: center;
  }
  .card-back .brand-square {
    position: absolute;
    left: 223px;
    top: 36px;
    width: 80px;
    height: 80px;
    background: var(--ink);
  }
  .card-back .brand-name {
    position: absolute;
    left: 0;
    top: 166px;
    width: 100%;
  }
  .card-back .brand-main {
    font-size: 48px;
    letter-spacing: 3px;
  }
  .card-back .brand-sub {
    font-size: 13px;
    letter-spacing: 5.5px;
    margin-top: 8px;
  }
  .card-back .website-wide {
    position: absolute;
    left: 0;
    top: 250px;
    width: 100%;
    font-size: 13px;
    letter-spacing: 3.6px;
    color: var(--ink);
  }
</style>
</head>
<body>

  <section class="card card-front" aria-label="Business card front">
    <div class="info-band"></div>
    <svg class="band-notch" viewBox="0 0 34 18" aria-hidden="true">
      <polygon points="0,0 34,0 17,18" fill="#ffffff"/>
    </svg>

    <div class="brand-lockup">
      <div class="brand-dot"></div>
      <div class="brand-name">
        <span class="brand-main">CORVANE</span>
        <span class="brand-sub">BROKERAGE SERVICES</span>
      </div>
    </div>

    <div class="contact-person">
      <div><span class="person-name">John Doe</span><span class="person-role">Manager</span></div>
      <div class="contact-lines">
        <div><span class="label">Mobile:</span> 000 000 000</div>
        <div><span class="label">Email:</span> john@corvanebrokerage.com</div>
      </div>
      <div class="website">www.CorvaneBrokerage.com</div>
    </div>

    <div class="column-rule"></div>

    <address class="contact-address" style="font-style: normal;">
      <div>00 Your Street</div>
      <div>000000 000 000 0000</div>
      <div>PO Box 000</div>
      <div class="phones">
        <div><span class="label">Ph:</span> +00 7 0000 0000</div>
        <div><span class="label">Fax:</span> + 00 7 0000 0000</div>
      </div>
    </address>
  </section>

  <section class="card card-back" aria-label="Business card back">
    <div class="brand-square"></div>
    <div class="brand-name">
      <span class="brand-main">CORVANE</span>
      <span class="brand-sub">BROKERAGE SERVICES</span>
    </div>
    <div class="website-wide">www.CorvaneBrokerage.com</div>
  </section>

</body>
</html>
```